Business Card Design Project

Basketball Training program

Offers: Travel Club Program - Camps - Clinics - Private Training

website: ridgeportcourt.net
Phone Contact: Main Phone: 555-314-7720
Email: ridgeport.court@mailzone.example

Industry/Entity Type

Business

Contact Information for Business Card

Need one for the following coaches:
Marcus Thorne - Boys & Girls Basketball Coach
Kirasol Vendry - Girls Basketball Coach
Anselmo Trujar - Director/Head Coach
Walter Fisk- Boys Basketball
Howard Lindqvist - Boys Basketball
Ramon Etxeberri - Boys Basketball
Talvin Okafor- Boys Basketball/ Trainer
Al Hargrove - Boys & Girls Basketball Coach

Basketball Training program Logo - one side

Logo on the corner
new one on the left (RC)
old one on the right (old one is with the ridgeport and court)

```html
<!DOCTYPE html>
<html lang="en">
<head>
<meta charset="utf-8">
<title>Ridgeport Court – Business Card</title>
<link href="https://fonts.googleapis.com/css2?family=Open+Sans:wght@400;600;700;800&display=swap" rel="stylesheet">
<style>
  :root {
    --page-bg: #2b2b2d;
    --card-black: #060606;
    --brand-yellow: #fdb813;
    --brand-grey: #6f6f72;
    --text-white: #f2f2f2;
  }
  * { box-sizing: border-box; margin: 0; padding: 0; }
  html, body { width: 1200px; height: 900px; overflow: hidden; }
  body {
    background: var(--page-bg);
    font-family: "Open Sans", Arial, sans-serif;
    position: relative;
  }
  .card {
    position: absolute;
    left: 250px;
    width: 700px;
    height: 400px;
    background: var(--card-black);
    border-radius: 26px;
    overflow: hidden;
  }
  .card-front { top: 40px; }
  .card-back { top: 470px; }

  /* Front */
  .front-mark {
    position: absolute;
    left: 50%;
    top: 58px;
    transform: translateX(-50%);
    display: flex;
    flex-direction: column;
    align-items: center;
  }
  .front-mark .mark-circle {
    width: 210px; height: 210px;
    border-radius: 50%;
    border: 22px solid var(--brand-grey);
    display: flex; align-items: center; justify-content: center;
  }
  .front-mark .mark-name {
    font-size: 86px; font-weight: 800; color: var(--brand-yellow); letter-spacing: 2px;
  }
  .front-web {
    position: absolute;
    left: 0; right: 0; top: 312px;
    text-align: center;
    color: var(--brand-yellow);
    font-size: 20px; font-weight: 600; letter-spacing: 0.5px;
  }

  /* Back */
  .back-logo {
    position: absolute;
    left: 40px; top: 105px;
    width: 290px; height: 190px;
    display: flex; align-items: center; gap: 14px;
  }
  .back-logo .logo-dot {
    width: 70px; height: 70px; border-radius: 50%;
    background: var(--brand-yellow); flex: none;
  }
  .back-logo .logo-name {
    color: var(--brand-yellow);
    font-size: 30px; font-weight: 800; line-height: 1.05; text-transform: uppercase;
  }
  .divider {
    position: absolute;
    left: 352px; top: 80px;
    width: 2px; height: 240px;
    background: var(--brand-yellow);
  }
  .details {
    position: absolute;
    left: 380px; top: 88px;
    color: var(--text-white);
  }
  .person-name {
    color: var(--brand-yellow);
    font-size: 27px; font-weight: 800; letter-spacing: 0.5px; text-transform: uppercase; line-height: 1.1;
  }
  .person-role {
    font-size: 13px; font-weight: 400; text-transform: uppercase; margin-bottom: 10px;
  }
  .contact-list, .service-list { list-style: none; }
  .contact-list li {
    display: flex; align-items: center; gap: 8px;
    font-size: 13.5px; line-height: 22px;
  }
  .contact-list svg { width: 12px; height: 12px; flex: none; }
  .service-list { margin-top: 10px; }
  .service-list li {
    display: flex; align-items: center; gap: 9px;
    font-size: 14px; line-height: 20px; text-transform: uppercase;
  }
  .service-list li::before {
    content: ""; width: 10px; height: 10px; border-radius: 50%;
    background: var(--brand-yellow); flex: none;
  }
</style>
</head>
<body>

<section class="card card-front">
  <div class="front-mark">
    <div class="mark-circle"><span class="mark-name">RC</span></div>
  </div>
  <p class="front-web">www.ridgeportcourt.net</p>
</section>

<section class="card card-back">
  <div class="back-logo">
    <span class="logo-dot"></span>
    <span class="logo-name">Ridgeport<br>Court</span>
  </div>
  <div class="divider"></div>
  <div class="details">
    <h1 class="person-name">Marcus Thorne</h1>
    <p class="person-role">Boys &amp; Girls Basketball Coach</p>
    <ul class="contact-list">
      <li>
        <svg viewBox="0 0 24 24" fill="var(--brand-yellow)"><path d="M6.6 10.8a15 15 0 0 0 6.6 6.6l2.2-2.2c.3-.3.7-.4 1-.2 1.1.4 2.3.6 3.6.6.6 0 1 .4 1 1V20c0 .6-.4 1-1 1C10.6 21 3 13.4 3 4c0-.6.4-1 1-1h3.5c.6 0 1 .4 1 1 0 1.3.2 2.5.6 3.6.1.3 0 .7-.2 1z"/></svg>
        555-314-7720
      </li>
      <li>
        <svg viewBox="0 0 24 24" fill="none" stroke="var(--brand-yellow)" stroke-width="2.4"><rect x="3" y="5" width="18" height="14" rx="1"/><path d="M3 6l9 7 9-7"/></svg>
        ridgeport.court@mailzone.example
      </li>
      <li>
        <svg viewBox="0 0 24 24" fill="none" stroke="var(--brand-yellow)" stroke-width="2.2"><circle cx="12" cy="12" r="9"/><path d="M3 12h18M12 3c3 3 3 15 0 18M12 3c-3 3-3 15 0 18"/></svg>
        www.ridgeportcourt.net
      </li>
    </ul>
    <ul class="service-list">
      <li>Travel Club Program</li>
      <li>Camps</li>
      <li>Clinics</li>
      <li>Private Training</li>
    </ul>
  </div>
</section>

</body>
</html>
```